Conceptual Model Diagram for Replacing Medication with Behavior to Support Weight Loss Maintenance

Design a figure of a conceptual model that needs to be inserted into a word document for a PSF grant. This conceptual model illustrates how behavioral strategies can replace the regulatory functions lost after AOM discontinuation. The intervention targets three core vulnerabilities—appetite resurgence, metabolic inflexibility, and suboptimal mindstate—through the domains of Food, Physical Activity, and Mind. Sustained weight loss maintenance occurs at the intersection of these domains. The intervention is delivered within a design framework that makes behaviors easier to perform, aligns them with identity, and reinforces them through virtual support and community, ensuring real-world feasibility and long-term adherence.
Target Market(s)
PSF reviewers
Industry/Entity Type
academic
Other font styles liked:
- arial
Requirements
Must have
- see my attached description

```html
<!DOCTYPE html>
<html lang="en">
<head>
<meta charset="utf-8">
<title>Conceptual Model: Replacing Medication with Behavior for Weight Loss Maintenance</title>
<link rel="stylesheet" href="https://fonts.googleapis.com/css2?family=Arimo:wght@400;700&display=swap">
<style>
  :root {
    --ring-outer: #b0b1b4;
    --ring-middle: #c8c9cb;
    --ring-inner: #e6e7e8;
    --paper: #ffffff;
    --teal: #12bab5;
    --domain-blue: #216995;
    --overlap-blue: #1f4a70;
    --core-blue: #283d68;
    --ink: #111111;
    --light-text: #ffffff;
  }
  html, body {
    margin: 0;
    padding: 0;
    width: 957px;
    height: 1200px;
    overflow: hidden;
    background: var(--paper);
  }
  .model-figure {
    display: block;
    width: 957px;
    height: 1200px;
    font-family: "Arimo", Arial, sans-serif;
  }
  .ring--outer { fill: var(--ring-outer); }
  .ring--middle { fill: var(--ring-middle); }
  .ring--inner { fill: var(--ring-inner); }
  .ring--core { fill: var(--paper); }
  .vulnerability { fill: var(--teal); }
  .domain { fill: var(--domain-blue); }
  .overlap { fill: var(--overlap-blue); }
  .overlap--core { fill: var(--core-blue); }
  .divider { stroke: var(--paper); stroke-width: 5; }
  .layer-title { font-weight: 700; font-size: 46px; fill: var(--ink); }
  .layer-detail { font-weight: 400; font-size: 40px; fill: var(--ink); }
  .vulnerability-label { font-weight: 700; font-size: 40px; fill: var(--light-text); }
  .domain-label { font-weight: 400; font-size: 50px; fill: var(--light-text); }
  .outcome-label { font-weight: 700; font-size: 46px; fill: var(--light-text); }
  .caption { font-weight: 400; font-size: 34px; fill: var(--ink); }
</style>
</head>
<body>
<svg class="model-figure" viewBox="0 0 1722 2160" xmlns="http://www.w3.org/2000/svg" role="img" aria-label="Conceptual model for sustained weight loss maintenance after medication discontinuation">
  <defs>
    <path id="arc-layer3-top" d="M 160 887 A 700 700 0 0 1 1560 887"/>
    <path id="arc-layer2-top" d="M 265 887 A 595 595 0 0 1 1455 887"/>
    <path id="arc-layer1-top" d="M 370 887 A 490 490 0 0 1 1350 887"/>
    <path id="arc-layer1-bottom" d="M 320 887 A 540 540 0 0 0 1400 887"/>
    <path id="arc-layer2-bottom" d="M 220 887 A 640 640 0 0 0 1500 887"/>
    <path id="arc-layer3-bottom" d="M 115 887 A 745 745 0 0 0 1605 887"/>
    <path id="arc-mindstate" d="M 716 1065 A 255 255 0 1 1 946 682"/>
    <path id="arc-appetite" d="M 837 611 A 255 255 0 0 1 1155 1013"/>
    <path id="arc-metabolic" d="M 577 1045 A 283 283 0 0 0 1143 1045"/>
    <clipPath id="clip-mind"><circle cx="725" cy="810" r="200"/></clipPath>
    <clipPath id="clip-food"><circle cx="997" cy="810" r="200"/></clipPath>
    <clipPath id="clip-activity"><circle cx="860" cy="1045" r="200"/></clipPath>
  </defs>

  <g class="framework-rings">
    <circle class="ring--outer" cx="860" cy="887" r="772"/>
    <circle class="ring--middle" cx="860" cy="887" r="665"/>
    <circle class="ring--inner" cx="860" cy="887" r="560"/>
    <circle class="ring--core" cx="860" cy="887" r="455"/>
  </g>

  <g class="framework-titles">
    <text class="layer-title"><textPath href="#arc-layer3-top" startOffset="50%" text-anchor="middle">3. Virtual Support and Social Connection</textPath></text>
    <text class="layer-title"><textPath href="#arc-layer2-top" startOffset="50%" text-anchor="middle">2. Align with Identity</textPath></text>
    <text class="layer-title"><textPath href="#arc-layer1-top" startOffset="50%" text-anchor="middle">1. Make it Easy</textPath></text>
    <text class="layer-detail"><textPath href="#arc-layer1-bottom" startOffset="50%" text-anchor="middle">(Habits, Routines, Environment, Low Friction)</textPath></text>
    <text class="layer-detail"><textPath href="#arc-layer2-bottom" startOffset="50%" text-anchor="middle">(Self-Concept, Maintain IT Model, Internalization)</textPath></text>
    <text class="layer-detail"><textPath href="#arc-layer3-bottom" startOffset="50%" text-anchor="middle">(Accessibility, Community, Shared Accountability)</textPath></text>
  </g>

  <g class="vulnerabilities">
    <circle class="vulnerability" cx="725" cy="810" r="298"/>
    <circle class="vulnerability" cx="997" cy="810" r="298"/>
    <circle class="vulnerability" cx="860" cy="1045" r="298"/>
  </g>

  <g class="domains">
    <circle class="domain" cx="725" cy="810" r="200"/>
    <circle class="domain" cx="997" cy="810" r="200"/>
    <circle class="domain" cx="860" cy="1045" r="200"/>
    <circle class="overlap" cx="997" cy="810" r="200" clip-path="url(#clip-mind)"/>
    <circle class="overlap" cx="860" cy="1045" r="200" clip-path="url(#clip-mind)"/>
    <circle class="overlap" cx="860" cy="1045" r="200" clip-path="url(#clip-food)"/>
    <g clip-path="url(#clip-mind)">
      <circle class="overlap--core" cx="997" cy="810" r="200" clip-path="url(#clip-activity)"/>
    </g>
  </g>

  <g class="pointers">
    <polygon class="vulnerability" points="568,680 592,736 532,742 520,700"/>
    <polygon class="vulnerability" points="1152,680 1128,736 1188,742 1200,700"/>
    <polygon class="vulnerability" points="822,1245 860,1198 898,1245 860,1260"/>
  </g>

  <g class="dividers">
    <line class="divider" x1="860" y1="535" x2="860" y2="665"/>
    <line class="divider" x1="560" y1="1062" x2="667" y2="1000"/>
    <line class="divider" x1="1160" y1="1062" x2="1053" y2="1000"/>
  </g>

  <g class="vulnerability-labels">
    <text class="vulnerability-label"><textPath href="#arc-mindstate" startOffset="50%" text-anchor="middle">Suboptimal Mindstate</textPath></text>
    <text class="vulnerability-label"><textPath href="#arc-appetite" startOffset="50%" text-anchor="middle">Appetite Resurgence</textPath></text>
    <text class="vulnerability-label"><textPath href="#arc-metabolic" startOffset="50%" text-anchor="middle">Metabolic Inflexibility</textPath></text>
  </g>

  <g class="domain-labels">
    <text class="domain-label" x="683" y="808" text-anchor="middle">Mind</text>
    <text class="domain-label" x="1040" y="808" text-anchor="middle">Food</text>
    <text class="domain-label" x="860" y="1080" text-anchor="middle">Physical</text>
    <text class="domain-label" x="860" y="1132" text-anchor="middle">Activity</text>
  </g>

  <g class="outcome">
    <text class="outcome-label" x="860" y="860" text-anchor="middle">Sustained</text>
    <text class="outcome-label" x="860" y="907" text-anchor="middle">Weight Loss</text>
    <text class="outcome-label" x="860" y="954" text-anchor="middle">Maintenance</text>
  </g>

  <g class="figure-caption">
    <text class="caption" x="90" y="1805">This conceptual model illustrates how behavioral strategies can replace the regulatory functions lost</text>
    <text class="caption" x="90" y="1852">after AOM discontinuation. The intervention targets three core vulnerabilities—appetite resurgence,</text>
    <text class="caption" x="90" y="1899">metabolic inflexibility, and suboptimal mindstate—through the domains of Food, Physical Activity,</text>
    <text class="caption" x="90" y="1946">and Mind. Sustained weight loss maintenance occurs at the intersection of these domains. The</text>
    <text class="caption" x="90" y="1993">intervention is delivered within a design framework that makes behaviors easier to perform, aligns</text>
    <text class="caption" x="90" y="2040">them with identity, and reinforces them through virtual support and community, ensuring real-world</text>
    <text class="caption" x="90" y="2087">feasibility and long-term adherence.</text>
  </g>
</svg>
</body>
</html>
```